Stationery Design Project - Ta fourmilière

We are a french company, Ta Fourmilière. It means Your Anthill.
We own and manage woods, we transform it industrially into very high quality (dry) logs and pellets and we commercialize them to individuals in France.
People can order the logs online or by phone and get the wood logs delivered at home.

After our great logo contest, we would like to launch a new stationery project.

Target Market(s)

inhabitants of sub-urban areas in France. (living in houses not in apartment )

Industry/Entity Type

It Company

Requirements
Must have
• content see attachment
logo

For the business card, we would like on the front side, the logo, name + contact info. We would like to use the back side for commercial purpose insisting on our distinctive value proposition.
Nice to have
• the back side of the business card can be more colorful

```html
<!DOCTYPE html>
<html lang="fr">
<head>
<meta charset="utf-8">
<title>Ta Fourmilière — Letterhead</title>
<link href="https://fonts.googleapis.com/css2?family=Montserrat:wght@400;500;700;800&display=swap" rel="stylesheet">
<style>
  :root {
    --backdrop: #2b2b2b;
    --paper: #ffffff;
    --paper-shade: #eeeeee;
    --ink: #2e2e2e;
    --ink-soft: #555555;
    --brand-red: #c8102e;
    --brand-navy: #14263d;
    --signature-blue: #1f3fa8;
    --figure-red: #b3242c;
    --figure-skin: #c99a74;
    --figure-wood: #b99572;
  }
  * { box-sizing: border-box; margin: 0; padding: 0; }
  html, body {
    width: 1200px; height: 900px; overflow: hidden;
    background: var(--backdrop);
    font-family: "Montserrat", Arial, sans-serif;
  }
  .letterhead {
    position: absolute; left: 300px; top: 26px;
    width: 600px; height: 848px;
    background: linear-gradient(160deg, var(--paper) 40%, var(--paper-shade) 100%);
    overflow: hidden;
  }
  .letterhead__brand {
    position: absolute; left: 54px; top: 92px;
    font-weight: 800; font-size: 34px; letter-spacing: -1.5px;
    color: var(--ink);
  }
  .letterhead__contact {
    position: absolute; left: 380px; top: 40px;
    font-size: 8px; line-height: 1.45; color: var(--ink-soft); font-weight: 500;
    list-style: none;
  }
  .letterhead__contact b { color: var(--brand-red); font-weight: 700; margin-right: 6px; }
  .letterhead__body {
    position: absolute; left: 96px; top: 286px; width: 420px;
    font-size: 10.5px; line-height: 1.42; color: var(--ink);
  }
  .letterhead__body p { margin-bottom: 13px; text-align: justify; }
  .letterhead__signature {
    position: absolute; left: 100px; top: 644px; width: 150px; height: 30px;
    background: linear-gradient(90deg, rgba(31,63,168,0.35), rgba(31,63,168,0.12));
    border-radius: 15px;
  }
  .letterhead__role {
    position: absolute; left: 118px; top: 678px;
    font-size: 12px; line-height: 1; color: var(--ink);
  }
  .letterhead__swoosh { position: absolute; left: 0; top: 0; }
  .letterhead__mascot {
    position: absolute; left: 28px; top: 704px; width: 210px; height: 144px;
    background: linear-gradient(180deg, var(--figure-wood) 0%, var(--figure-skin) 35%, var(--figure-red) 75%);
    border-radius: 80px 80px 0 0;
  }
</style>
</head>
<body>
  <main class="letterhead">
    <svg class="letterhead__swoosh" width="600" height="848" viewBox="0 0 600 848" aria-hidden="true">
      <path d="M0 812 C210 790 420 770 600 668 L600 848 L0 848 Z" fill="#d9d9d9"/>
      <path d="M0 822 C210 800 420 782 600 684 L600 848 L0 848 Z" fill="var(--brand-red)"/>
      <path d="M330 772 C450 748 540 708 600 652 L600 672 C540 720 450 760 330 772 Z" fill="var(--brand-navy)"/>
    </svg>

    <div class="letterhead__brand">Ta Fourmilière</div>

    <ul class="letterhead__contact">
      <li>14 Chemin des Pins 69500 Vaugrenoux</li>
      <li><b>Tel:</b>04 00 12 34 56</li>
      <li><b>Email:</b>info@tafourmiliere.fr</li>
      <li><b>Web:</b>www.tafourmiliere.fr</li>
    </ul>

    <section class="letterhead__body">
      <p>Letterhead samples are a great way of deciding what kind of letterhead you want to design for you and your company. The internet has a ton of great letterhead samples to browse through. Whether you want something simple, with just a couple lines of text of your business information, or something decorative and stunning, with photos and logos on the top and bottom of the page, it will be easy to find what you want, because there are samples online for basically any type of letterhead you could want.</p>
      <p>Any business could easily benefit from browsing through some letterhead samples, if only to get an idea for what kind of letterhead their company might want. Letterheads are just one of the tools that a business professional could use to help increase their customer base, and to really be memorable to everyone they write a letter to. Letterhead is quite an effective tool for marketing and advertising, but because it's such a simple and well known idea, it is often unfairly overlooked. Make sure you don't make that mistake, and make some letterhead samples of your own today.</p>
      <p>Whether you want to get new customers to remember you and become part of your clientele, or you just want to send out friendly reminders to your existing clients, customizing your own letterhead samples can really help you out. Try out some letterhead samples and you will not regret it, and I'm sure you will add a new tool to your business' arsenal of networking, marketing, and advertising tools.</p>
    </section>

    <div class="letterhead__signature" role="img" aria-label="Handwritten signature of Paul Renard"></div>
    <div class="letterhead__role">company director</div>

    <div class="letterhead__mascot" role="img" aria-label="Illustration of a lumberjack in a red checked shirt holding a tray of firewood logs"></div>
  </main>
</body>
</html>
```